Valmora Engineering Pty Ltd - designed for architects to look at products

We need a web design which is modern and stands out. Our company will distribute electronic drives to Australia and New Zealand. The company is called Valmora Engineering. This website will be looked at by architects and manufacturers that will use or specify this product in the healthcare industry, automotive industry and food processing industry. Our product is designed to automate things such as wheelchairs, windows, hospital beds ect. We get our product from the manufacturer in Denmark called 'Brivan'.
I need someone to take all the information and the logo from their website but change the way it is set up and the colours. We dont want to use their contact information.
www.brivan-example.com
Pictures must be used too.
Contact information below;

Valmora Engineering PTY LTD
ACN (Australian Company Number): 482 615 307
Postal Address: PO Box 4718, Kelby Flats, Western Australia 6071
hal@valmora-example.com.au
ross@valmora-example.com.au

Phone Fax
0291546612 0291546623 Sydney

0354189902 0354189903 Melbourne

0746251194 0746251105 Brisbane

0871493305 0871493316 Adelaide

0861734420 0861734421 Perth

038526703 038526704 Christchurch

094637361 094637362 Auckland

Target Market(s)

Architects, engineers and manufacturers

Industry/Entity Type

Automotive

Requirements
Must have
• Please include all case studies with photos from the brivan website www.brivan-example.com.au
I do not want this website looking anything like theirs please
Should not have
• No links to facebook, twitter or any other sites like that

```html
<!DOCTYPE html>
<html lang="en">
<head>
<meta charset="utf-8">
<title>Tarvel Hatches Pty Ltd</title>
<link href="https://fonts.googleapis.com/css2?family=Ubuntu:wght@400;500&family=Arimo&display=swap" rel="stylesheet">
<style>
:root{
  --red:#b3141f;
  --red-dark:#6e0710;
  --grey-dark:#3c3c3c;
  --grey-mid:#6a6a6a;
  --page-top:#ececee;
  --page-low:#c9c7d1;
  --text:#222;
  --muted:#9a9a9a;
  --white:#fff;
}
*{margin:0;padding:0;box-sizing:border-box}
html,body{width:942px;height:1200px;overflow:hidden}
body{position:relative;font-family:"Ubuntu",sans-serif;color:var(--text);
  background:linear-gradient(180deg,#e4e4e6 0,#f1f1f3 124px,#e8e8ea 164px,#e6e5e9 315px,var(--page-low) 315px,#cfcdd6 1011px,#f4f4f4 1011px)}
.abs{position:absolute}
.header{left:0;top:0;width:942px;height:124px;background:linear-gradient(120deg,#dcdcdf 0,#f4f4f6 30%,#c9c9cd 55%,#ededf0 75%,#d7d7db 100%)}
.logo{left:62px;top:18px;width:178px;height:99px;background:var(--white);border-radius:4px;box-shadow:0 1px 3px rgba(0,0,0,.2);display:flex;align-items:center;justify-content:center;gap:8px}
.logo .mark{width:14px;height:14px;background:var(--red)}
.logo span{font-weight:500;font-size:20px;color:var(--red)}
.search{left:726px;top:55px;width:142px;height:29px;display:flex}
.search .field{flex:1;background:var(--white);font-size:13px;color:#888;padding:7px 0 0 27px;border-radius:3px 0 0 3px}
.search .btn{width:33px;background:var(--red);border-radius:0 3px 3px 0;display:flex;align-items:center;justify-content:center}
.nav{left:0;top:124px;width:942px;height:40px;background:linear-gradient(#fafafa,#ededed);border-bottom:1px solid #d4d4d4}
.nav a{position:absolute;top:11px;font-size:13px;color:#333;text-decoration:none;transform:translateX(-50%)}
.nav .home{left:60px;top:3px;width:72px;height:32px;background:linear-gradient(#c8262e,#9c0d16);color:#fff;border-radius:3px;transform:none;text-align:center;line-height:32px}
.nav .sep{position:absolute;top:0;width:1px;height:40px;background:#d0d0d0}
.slider{left:60px;top:189px;width:806px;height:315px;background:#8a8a8a;border-radius:2px}
.slide{left:7px;top:7px;width:792px;height:302px;background:linear-gradient(135deg,#e9ecec 0,#cfd6d8 40%,#8fc9d4 60%,#d9dcdc 80%,#b5b8b8 100%)}
.caption{left:188px;top:246px;font-size:16px;line-height:32px;color:#111}
.arrow{top:133px;width:38px;height:53px;background:#1d1d1d;display:flex;align-items:center;justify-content:center}
.arrow i{width:22px;height:22px;border-radius:50%;background:#f3f3f3;display:flex;align-items:center;justify-content:center}
.arrow.prev{left:-7px;border-radius:0 27px 27px 0}
.arrow.next{right:-7px;border-radius:27px 0 0 27px}
.main{left:60px;top:520px;width:806px;height:491px;background:var(--white);border-radius:3px;box-shadow:0 0 6px rgba(0,0,0,.08)}
.panel{left:77px;width:214px;color:#fff;border-radius:10px 10px 0 0}
.panel h2{font-weight:400;font-size:17px;padding:13px 0 0 17px;height:42px;border-bottom:1px solid rgba(255,255,255,.45)}
.contact{top:540px;height:254px;background:linear-gradient(#c01a26,var(--red-dark))}
.contact p{font-size:11px;line-height:17.8px;padding:10px 0 0 23px}
.services{top:808px;height:182px;background:linear-gradient(var(--grey-mid),var(--grey-dark))}
.services ul{list-style:none;padding:7px 0 0 17px}
.services li{font-size:11px;line-height:21.3px;display:flex;align-items:center;gap:8px}
.title{font-weight:400;font-size:21px;color:#333}
.title em{font-style:normal;color:var(--red)}
.chair{left:342px;top:587px;width:147px;height:177px;background:radial-gradient(circle at 50% 45%,#3d5a8a 0,#2a2f3a 40%,#dfe2e6 75%,#fff 100%)}
.intro{left:510px;top:609px;width:340px;font-size:9.8px;line-height:17.8px;color:#222}
.dots{left:340px;top:776px;width:482px;border-top:1px dotted #777}
.card{top:826px;width:112px;height:118px;border:1px solid #cfcfcf;border-radius:3px;background:#fff;box-shadow:0 1px 3px rgba(0,0,0,.12);padding:12px}
.card div{width:100%;height:100%}
.label{top:956px;width:130px;text-align:center;font-size:11.5px;line-height:15.5px;color:#444}
.phones{left:60px;top:1027px;width:806px;height:100px;background:linear-gradient(#4a4a4a,#2f2f2f);border-radius:2px;color:#fff}
.phones h3{position:absolute;left:40px;top:42px;font-weight:400;font-size:17px}
.phones .col{position:absolute;font-size:12.5px;line-height:20.5px;letter-spacing:.3px}
.phones span{color:var(--muted)}
.footnav{left:0;top:1140px;width:942px;text-align:center;font-size:11.5px;color:#222;word-spacing:2px}
.copy{left:0;top:1172px;width:942px;text-align:center;font-family:"Arimo",sans-serif;font-size:11px;color:#222}
</style>
</head>
<body>
<div class="abs header"></div>
<div class="abs logo"><i class="mark"></i><span>Tarvel Hatches Pty Ltd</span></div>
<div class="abs search"><div class="field">Search</div><div class="btn"><svg width="18" height="18" viewBox="0 0 18 18"><circle cx="7" cy="7" r="5" fill="none" stroke="#fff" stroke-width="2"/><path d="M11 11l5 5" stroke="#fff" stroke-width="3"/></svg></div></div>

<nav class="abs nav">
  <a class="home" href="#">Home</a>
  <a href="#" style="left:196px">About Us</a><i class="sep" style="left:244px"></i>
  <a href="#" style="left:303px">Products</a><i class="sep" style="left:352px"></i>
  <a href="#" style="left:398px">Links</a><i class="sep" style="left:442px"></i>
  <a href="#" style="left:492px">Services</a><i class="sep" style="left:540px"></i>
  <a href="#" style="left:599px">Contact Us</a>
</nav>

<section class="abs slider">
  <div class="abs slide" role="img" aria-label="Photo of an adjustable hospital bed with blue head and foot boards"></div>
  <p class="abs caption">Lorem ipsum dolor sit amet, consectetuer adipiscing elit.<br>Nam nibh. Nunc varius facilisis eros.</p>
  <div class="abs arrow prev"><i><svg width="8" height="10"><path d="M2 1l4 4-4 4" fill="none" stroke="#333" stroke-width="1.5"/></svg></i></div>
  <div class="abs arrow next"><i><svg width="8" height="10"><path d="M6 1L2 5l4 4" fill="none" stroke="#333" stroke-width="1.5"/></svg></i></div>
</section>

<div class="abs main"></div>

<aside class="abs panel contact">
  <h2>Our Contact</h2>
  <p>Valmora Engineering PTY LTD<br>ACN (Australian Company<br>Number): 482 615 307<br><br>Postal Address:<br>PO Box 4718, Kelby Flats,<br>Western Australia 6071<br><br>hal@valmora-example.com.au<br>ross@valmora-example.com.au</p>
</aside>

<aside class="abs panel services">
  <h2>Our Services</h2>
  <ul>
    <li><svg width="9" height="10"><path d="M8 1L2 5l6 4" fill="none" stroke="#aaa" stroke-width="2"/></svg>Roof hatches</li>
    <li><svg width="9" height="10"><path d="M8 1L2 5l6 4" fill="none" stroke="#aaa" stroke-width="2"/></svg>Wall and ceiling doors</li>
    <li><svg width="9" height="10"><path d="M8 1L2 5l6 4" fill="none" stroke="#aaa" stroke-width="2"/></svg>Fire rated hatches and doors</li>
    <li><svg width="9" height="10"><path d="M8 1L2 5l6 4" fill="none" stroke="#aaa" stroke-width="2"/></svg>Explosion vents</li>
    <li><svg width="9" height="10"><path d="M8 1L2 5l6 4" fill="none" stroke="#aaa" stroke-width="2"/></svg>Ladders and stairs</li>
    <li><svg width="9" height="10"><path d="M8 1L2 5l6 4" fill="none" stroke="#aaa" stroke-width="2"/></svg>Floor doors - hinged</li>
  </ul>
</aside>

<h1 class="abs title" style="left:337px;top:552px">Welcome to <em>Tarvel</em></h1>
<div class="abs chair" role="img" aria-label="Photo of a tilting wheelchair with blue and black padding"></div>
<p class="abs intro">Lorem Ipsum is simply dummy text of the printing and typesetting industry. Lorem Ipsum has been the industry's standard dummy text ever since the 1500s, when an unknown printer took a galley of type and scrambled it to make a type specimen book.Lorem Ipsum is simply dummy text of the printing and typesetting industry. Lorem Ipsum has been the industry's standard dummy text ever since the 1500s, when an unknown printer took a galley of type and scrambled it to make a type specimen book.</p>
<div class="abs dots"></div>

<h2 class="abs title" style="left:336px;top:789px">Our &nbsp;<em>Products</em></h2>
<svg class="abs" style="left:311px;top:869px" width="20" height="22"><path d="M17 2L5 11l12 9" fill="none" stroke="#b3141f" stroke-width="5"/></svg>
<svg class="abs" style="left:837px;top:869px" width="20" height="22"><path d="M3 2l12 9-12 9" fill="none" stroke="#b3141f" stroke-width="5"/></svg>

<div class="abs card" style="left:336px"><div role="img" aria-label="Product photo of a roof hatch" style="background:linear-gradient(#f2f2f2,#f5e6a8)"></div></div>
<div class="abs card" style="left:461px"><div role="img" aria-label="Product photo of a folding loft ladder" style="background:linear-gradient(135deg,#e0908a,#f3f3f3)"></div></div>
<div class="abs card" style="left:588px"><div role="img" aria-label="Product photo of a fire rated hatch" style="background:linear-gradient(#5a5a5a,#c9c9c9)"></div></div>
<div class="abs card" style="left:721px"><div role="img" aria-label="Product photo of a detachable floor door" style="background:linear-gradient(#e2e2e2,#d9a7a0)"></div></div>
<p class="abs label" style="left:325px;top:957px">Roof hatches</p>
<p class="abs label" style="left:452px;top:957px">Ladders and stairs</p>
<p class="abs label" style="left:582px">Fire rated hatches<br>and doors</p>
<p class="abs label" style="left:714px">Floor doors –<br>detachable</p>

<section class="abs phones">
  <h3>Phone Fax</h3>
  <p class="col" style="left:179px;top:9px">0291546612 0291546623 <span>Sydney</span><br>0354189902 0354189903 <span>Melbourne</span><br>0746251194 0746251105 <span>Brisbane</span><br>0871493305 0871493316 <span>Adelaide</span></p>
  <p class="col" style="left:475px;top:19px">0861734420 0861734421 <span>Perth</span><br>038526703 038526704 <span>Christchurch</span><br>094637361 094637362 <span>Auckland</span></p>
</section>

<p class="abs footnav">Home &nbsp; | &nbsp; About Us &nbsp; | &nbsp; Products &nbsp;| &nbsp; Links &nbsp;| &nbsp; Services &nbsp; | &nbsp; Contact Us</p>
<p class="abs copy">Copyright © &nbsp;Tarvel, All Rights Reserved</p>
</body>
</html>
```